Business Card Design

We are state certified residental contractors who specialize in insurance claims. We are insurance restoration experts and have a state multi-lines insurance adjusters license #W584130. We produce insurance grade estimates using the most widely used software in the industry. Our goal is to work for our customers! not the insurance company. Our edge is we don't take short cuts to please the adjuster/insurance company to insure future claims from them. We are experts at restoring damaged properties.from wind, water ,fire and smoke. We pride ourselfs on evaluating damages properly and providing extremely detailed estimates for restoration.We are also educated and experienced in identifiying and correcting indoor air quality issues as a result of common perils and defective materials. .We are not a franchise and are family owned and operated. We provide quality work using only the best local tradesman. We ourselfs are local tradesmen and helped build and restore our community over the past 30 years. We know first hand how our homes were built and are aware of many of the common problems that exist and how to address them. We are licensed insured and bonded.
Industry/Entity Type
Business
Contact Information for Business Card
Beacon Harbor LLC
Marcus Pelley
4185 Willowbend Rd unit K
Melbourne Fl.32937 Manager/State Certified Residental Contractor license# CRC5871642
321-555-0187 Office
321-555-0162 Fax

```html
<!DOCTYPE html>
<html lang="en">
<head>
<meta charset="utf-8">
<title>Beacon Harbor LLC — Business Card</title>
<link href="https://fonts.googleapis.com/css2?family=Saira:wght@300&family=Teko:wght@300;400;500&display=swap" rel="stylesheet">
<style>
  :root {
    --backdrop: #d3d4d6;
    --card-light: #ffffff;
    --card-dark: #363435;
    --ink: #333132;
    --on-dark: #ffffff;
  }
  * { margin: 0; padding: 0; box-sizing: border-box; }
  html, body { width: 1200px; height: 1000px; overflow: hidden; background: var(--backdrop); }
  .canvas { position: relative; width: 1200px; height: 1000px; }

  .card { position: absolute; left: 256px; width: 688px; height: 397px; }
  .card--front { top: 70px; background: var(--card-light); }
  .card--back { top: 532px; background: var(--card-dark); }

  .brand__name {
    font-family: "Saira", sans-serif; font-weight: 300;
    font-size: 33px; line-height: 43px; color: var(--ink);
  }
  .card--front .brand { position: absolute; left: 165px; top: 136px; }

  .divider { position: absolute; left: 342px; top: 63px; width: 3px; height: 271px; background: var(--ink); }

  .contact { position: absolute; left: 381px; top: 84px; font-family: "Teko", sans-serif; color: var(--ink); }
  .contact__name { font-size: 38px; font-weight: 500; line-height: 38px; letter-spacing: 0.3px; }
  .contact__role { font-size: 20px; font-weight: 400; letter-spacing: 4px; line-height: 22px; }
  .contact__lines { margin-top: 12px; font-size: 21px; font-weight: 400; line-height: 28px; letter-spacing: 0.2px; }

  .license {
    position: absolute; left: 372px; right: 0; top: 281px; height: 28px;
    background: var(--ink); color: var(--on-dark);
    font-family: "Teko", sans-serif; font-size: 21px; font-weight: 400; line-height: 31px;
    letter-spacing: 3.5px; padding-left: 9px;
  }

  .card--back .brand {
    position: absolute; left: 0; right: 0; top: 160px;
    display: flex; justify-content: center;
  }
  .card--back .brand__name { color: var(--on-dark); font-size: 44px; line-height: 60px; }
</style>
</head>
<body>
<main class="canvas">
  <section class="card card--front" aria-label="Card front">
    <div class="brand">
      <p class="brand__name">Beacon<br>Harbor<br>LLC</p>
    </div>
    <div class="divider"></div>
    <div class="contact">
      <h1 class="contact__name">MARCUS PELLEY</h1>
      <p class="contact__role">MANAGER</p>
      <p class="contact__lines">
        4185 WILLOWBEND RD UNIT K MELBOURNE<br>
        FL.32937<br>
        PHONE : 321-555-0187<br>
        FAX : 321-555-0162
      </p>
    </div>
    <p class="license">LICENSE : CRC5871642</p>
  </section>

  <section class="card card--back" aria-label="Card back">
    <div class="brand">
      <p class="brand__name">Beacon Harbor LLC</p>
    </div>
  </section>
</main>
</body>
</html>
```